Redesign website for small print company

Vindaborgprent is a small printing company in Iceland mainly servicing Students, schools, etc. We are also doing all kind of other jobs, like business cards, book printing, brochure printing etc. We are also selling books online.
Our website is: www.vindaborgprent.is
What we are looking for is:
- Web Design (Uncoded - PSD layout only)
- Mobile friendly design, using our current color scheme: Red, green, yellow and light gray.
- Clean simple design
- Simple, light and easy to use.
- More menu Items/drop down
Industry/Entity Type
Digital Printing
Number of Pages Required
5+ page
Requirements
Must have
- Easy navigation
- Designed for mobile
- Current color scheme (see logo)
Nice to have
- Icon based products

```html
<!DOCTYPE html>
<html lang="en">
<head>
<meta charset="utf-8">
<title>Vindaborgprent</title>
<link href="https://fonts.googleapis.com/css2?family=Montserrat:wght@500;600;700;800&family=Lato:wght@400;700&display=swap" rel="stylesheet">
<style>
:root{
  --red:#e8312f;
  --green:#1e6b35;
  --yellow:#ffd500;
  --grey:#f4f4f4;
  --field:#e4e4e4;
  --ink:#1a1a1a;
  --muted:#666;
  --footer:#3b3b3b;
  --social:#8a8a8a;
  --white:#fff;
}
*{box-sizing:border-box;margin:0;padding:0}
html,body{width:1200px;height:3502px;overflow:hidden;background:var(--white)}
body{position:relative;font-family:'Lato',sans-serif;color:var(--ink)}
.abs{position:absolute}
.heading{font-family:'Montserrat',sans-serif;font-weight:700;text-transform:uppercase;letter-spacing:.5px}
.btn{position:absolute;background:var(--red);color:var(--white);font-family:'Montserrat',sans-serif;font-weight:600;font-size:11px;text-transform:uppercase;display:flex;align-items:center;justify-content:center;letter-spacing:.3px}
.mark{position:absolute;width:12px;height:12px;border-radius:50%;background:var(--red);left:594px}
.section-title{position:absolute;left:0;width:1200px;text-align:center;font-size:30px}

/* header */
.site-header{position:absolute;top:0;left:0;width:1200px;height:47px;background:var(--white)}
.menu-btn{position:absolute;left:160px;top:13px;width:24px;height:22px;border:1px solid #999;border-radius:3px;display:flex;flex-direction:column;justify-content:center;gap:3px;padding:0 5px}
.menu-btn span{height:2px;background:#333}
.login{left:222px;top:16px;font-size:12px;color:#333}
.brand{left:520px;top:10px;display:flex;align-items:center;gap:6px;font-family:'Montserrat',sans-serif;font-weight:800;font-size:19px;color:var(--ink)}
.brand i{width:20px;height:20px;background:var(--red);display:block}
.lang{left:904px;top:15px;width:50px;height:18px;border:1px solid #aaa;font-size:10px;display:flex;align-items:center;justify-content:center;gap:3px}
.lang b{width:14px;height:10px;background:#3b5fb0;display:block}

/* hero */
.hero{position:absolute;top:47px;left:0;width:1200px;height:607px;background:var(--grey)}
.hero-title{left:124px;top:205px;font-size:45px;line-height:52px;font-weight:800}
.hero-visual{left:590px;top:22px;width:560px;height:515px;background:linear-gradient(150deg,#4a4a4a,#151515 60%,#2c2c2c);border-radius:6px}
.dots{left:1096px;top:538px;display:flex;gap:8px}
.dots i{width:8px;height:8px;border-radius:50%;background:var(--yellow);display:block}
.dots i:first-child{background:var(--green)}
.feature-box{position:absolute;top:518px;width:240px;height:240px;display:flex;flex-direction:column;align-items:center;justify-content:center;text-align:center;gap:16px;font-family:'Montserrat',sans-serif;font-weight:700;text-transform:uppercase;font-size:17px;line-height:19px}
.feature-box small{display:block;font-size:12px;line-height:14px}
.box-yellow{left:173px;background:var(--yellow);color:var(--ink)}
.box-green{left:480px;background:var(--green);color:var(--white)}
.box-red{left:787px;background:var(--red);color:var(--white)}

/* products */
.tabs{left:0;width:1200px;top:916px;display:flex;justify-content:center;gap:26px;font-size:13px}
.tabs .active{color:var(--red);border-bottom:2px solid var(--red);padding-bottom:4px}
.product{position:absolute;top:988px;width:203px}
.product-cover{height:257px;background:#f2f2f2;display:flex;align-items:center;justify-content:center}
.product-cover div{width:108px;height:168px;box-shadow:4px 4px 8px rgba(0,0,0,.25)}
.product-name{font-family:'Montserrat',sans-serif;font-weight:700;font-size:13px;margin-top:20px}
.product-price{font-size:12px;color:var(--muted);margin-top:3px}

/* services */
.services{position:absolute;top:1448px;left:0;width:1200px;height:642px;background:var(--grey)}
.subtitle{left:0;width:1200px;text-align:center;font-size:13px;color:#444}
.service{position:absolute;width:220px;text-align:center}
.service svg{display:block;margin:0 auto}
.service p{font-family:'Montserrat',sans-serif;font-weight:700;font-size:13px;text-transform:uppercase;margin-top:12px}

/* about */
.welcome{left:163px;top:2265px;font-size:19px}
.about-text{left:163px;top:2310px;width:590px;font-size:12.5px;line-height:17px;color:#333}
.about-text p{margin-bottom:13px}
.about-brand{left:778px;top:2237px;width:233px;height:308px;background:var(--grey);display:flex;flex-direction:column;align-items:center;justify-content:center;gap:22px;font-family:'Montserrat',sans-serif;font-weight:800;font-size:21px;color:var(--ink)}
.about-brand i{width:90px;height:90px;background:var(--red);display:block}

/* contact */
.map{left:0;top:2638px;width:600px;height:540px;background:linear-gradient(135deg,#bfe0f5 0%,#cfe6f3 30%,#ececec 45%,#e6ead8 70%,#f3f0e6 100%)}
.contact-panel{left:600px;top:2638px;width:600px;height:540px;background:var(--grey)}
.field{position:absolute;left:717px;width:320px;background:var(--field);font-size:11px;color:#555;padding:12px 14px}
.note{left:600px;width:600px;text-align:center;font-size:12px;color:#444}

/* footer */
.site-footer{position:absolute;top:3180px;left:0;width:1200px;height:322px;background:var(--footer);color:var(--white)}
.footer-brand{left:163px;top:0;width:113px;height:112px;background:var(--white);display:flex;flex-direction:column;align-items:center;justify-content:center;gap:8px;font-family:'Montserrat',sans-serif;font-weight:800;font-size:11px;color:var(--ink)}
.footer-brand i{width:36px;height:36px;background:var(--red);display:block}
.footer-about{left:163px;top:136px;width:300px;font-size:12px;line-height:16px}
.footer-more{left:163px;top:196px;font-size:12px;color:var(--red);text-decoration:underline}
.social{left:163px;top:228px;display:flex;gap:6px}
.social i{width:16px;height:16px;display:block;border-radius:2px;background:var(--social)}
.footer-title{font-size:28px;top:92px}
.links{left:600px;top:150px;list-style:none;font-size:12px;line-height:19px}
.links li::before{content:"";display:inline-block;width:6px;height:6px;background:var(--yellow);margin-right:7px;vertical-align:middle}
.info{position:absolute;left:873px;display:flex;align-items:center;gap:14px;font-size:12px}
.rule{left:163px;top:264px;width:874px;height:1px;background:#777}
.copy{left:163px;top:284px;font-size:12px}
.cards{left:985px;top:285px;display:flex;gap:8px}
.cards i{width:24px;height:15px;background:var(--white);display:block;border-radius:2px}
</style>
</head>
<body>

<header class="site-header">
  <div class="menu-btn"><span></span><span></span><span></span></div>
  <div class="abs login">Login / Register</div>
  <div class="abs brand"><i></i>VINDABORGPRENT</div>
  <div class="abs lang"><b></b>EN ▾</div>
  <svg class="abs" style="left:982px;top:14px" width="18" height="18" viewBox="0 0 18 18"><circle cx="7.5" cy="7.5" r="5.5" fill="none" stroke="#333" stroke-width="2"/><line x1="11.5" y1="11.5" x2="16" y2="16" stroke="#333" stroke-width="2"/></svg>
  <svg class="abs" style="left:1018px;top:13px" width="20" height="20" viewBox="0 0 20 20"><path d="M1 2h3l2.5 10h10l2-7H5.5" fill="none" stroke="#333" stroke-width="2"/><circle cx="8" cy="16.5" r="1.6" fill="#333"/><circle cx="15" cy="16.5" r="1.6" fill="#333"/></svg>
</header>

<section class="hero">
  <h1 class="abs heading hero-title">No worries<br>....this reddast</h1>
  <div class="btn" style="left:124px;top:341px;width:105px;height:28px">Read more</div>
  <div class="abs hero-visual" role="img" aria-label="Black branded stationery set: folders, notebooks, cards, pens and envelopes"></div>
  <div class="abs dots"><i></i><i></i><i></i></div>
</section>

<div class="feature-box box-yellow">
  <svg width="70" height="62" viewBox="0 0 70 62"><rect x="16" y="2" width="38" height="18" fill="#111"/><rect x="2" y="20" width="66" height="26" rx="4" fill="#111"/><rect x="16" y="38" width="38" height="22" fill="#111" stroke="#ffd500" stroke-width="3"/><circle cx="58" cy="29" r="3" fill="#ffd500"/></svg>
  <div>Digital printing</div>
</div>
<div class="feature-box box-green">
  <svg width="40" height="60" viewBox="0 0 40 60"><path d="M4 2h32v56L20 44 4 58z" fill="#fff"/></svg>
  <div>Publishing<small>(copies, books, catalogues,<br>register, magazines,<br>notebooks)</small></div>
</div>
<div class="feature-box box-red">
  <svg width="56" height="66" viewBox="0 0 56 66"><path d="M14 38l-8 26 12-6 6 8 4-26zM42 38l8 26-12-6-6 8-4-26z" fill="#fff"/><circle cx="28" cy="24" r="22" fill="#fff"/><circle cx="28" cy="24" r="13" fill="none" stroke="#e8312f" stroke-width="3"/></svg>
  <div>Best quality<br>printing</div>
</div>

<div class="mark" style="top:817px"></div>
<h2 class="heading section-title" style="top:848px">Feature products</h2>
<div class="abs tabs"><span class="active">ALL</span><span>New</span><span>Best Seller</span></div>

<div class="product" style="left:163px"><div class="product-cover"><div role="img" aria-label="Black book cover" style="background:linear-gradient(160deg,#3a3a3a,#0f0f0f)"></div></div><div class="product-name">BOOK NAME</div><div class="product-price">$50</div></div>
<div class="product" style="left:388px"><div class="product-cover"><div role="img" aria-label="Turquoise book cover" style="background:linear-gradient(160deg,#3dc2d8,#1f9bb8)"></div></div><div class="product-name">BOOK NAME</div><div class="product-price">$50</div></div>
<div class="product" style="left:612px"><div class="product-cover"><div role="img" aria-label="Orange book cover" style="background:linear-gradient(160deg,#f59a2b,#d8421e)"></div></div><div class="product-name">BOOK NAME</div><div class="product-price">$50</div></div>
<div class="product" style="left:836px"><div class="product-cover"><div role="img" aria-label="Blue book cover" style="background:linear-gradient(160deg,#7fd0ea,#1d7fb6)"></div></div><div class="product-name">BOOK NAME</div><div class="product-price">$50</div></div>

<div class="btn" style="left:544px;top:1373px;width:108px;height:29px">View all</div>

<section class="services">
  <div class="mark" style="top:51px"></div>
  <h2 class="heading section-title" style="top:76px">Our services</h2>
  <div class="abs subtitle" style="top:122px">Lorem Ipsum is simply dummy text of the printing and typesetting industry.</div>

  <div class="service" style="left:161px;top:216px">
    <svg width="50" height="50" viewBox="0 0 50 50"><rect x="3" y="10" width="44" height="30" fill="#1e6b35"/><rect x="10" y="18" width="18" height="3" fill="#ffd500"/><rect x="10" y="25" width="26" height="3" fill="#ffd500"/></svg>
    <p>Business card</p></div>
  <div class="service" style="left:383px;top:216px">
    <svg width="50" height="50" viewBox="0 0 50 50"><rect x="10" y="3" width="30" height="44" fill="#ffd500" stroke="#1e6b35" stroke-width="3"/><rect x="16" y="13" width="18" height="3" fill="#1e6b35"/><rect x="16" y="21" width="18" height="3" fill="#1e6b35"/><rect x="16" y="29" width="18" height="3" fill="#1e6b35"/></svg>
    <p>Essays</p></div>
  <div class="service" style="left:593px;top:216px">
    <svg width="50" height="50" viewBox="0 0 50 50"><path d="M3 9l14-5 16 5 14-5v37l-14 5-16-5-14 5z" fill="#ffd500" stroke="#1e6b35" stroke-width="3" stroke-linejoin="round"/><line x1="17" y1="4" x2="17" y2="41" stroke="#1e6b35" stroke-width="3"/><line x1="33" y1="9" x2="33" y2="46" stroke="#1e6b35" stroke-width="3"/></svg>
    <p>Leafleats</p></div>
  <div class="service" style="left:812px;top:216px">
    <svg width="50" height="50" viewBox="0 0 50 50"><path d="M6 18l26-12 12 20-26 14z" fill="#1e6b35"/><path d="M6 18l12 22v5L6 23z" fill="#ffd500" stroke="#1e6b35" stroke-width="2"/></svg>
    <p>Books print</p></div>

  <div class="service" style="left:161px;top:388px">
    <svg width="50" height="50" viewBox="0 0 50 50"><rect x="5" y="9" width="40" height="36" fill="#ffd500" stroke="#1e6b35" stroke-width="3"/><rect x="5" y="9" width="40" height="9" fill="#1e6b35"/><rect x="13" y="3" width="4" height="10" fill="#1e6b35"/><rect x="33" y="3" width="4" height="10" fill="#1e6b35"/><g fill="#1e6b35"><rect x="11" y="23" width="6" height="5"/><rect x="22" y="23" width="6" height="5"/><rect x="33" y="23" width="6" height="5"/><rect x="11" y="33" width="6" height="5"/><rect x="22" y="33" width="6" height="5"/></g></svg>
    <p>Calander print</p></div>
  <div class="service" style="left:383px;top:388px">
    <svg width="50" height="50" viewBox="0 0 50 50"><rect x="9" y="4" width="32" height="42" fill="#ffd500" stroke="#1e6b35" stroke-width="3"/><path d="M13 40l10-14 7 9 4-5 4 10z" fill="#1e6b35"/><circle cx="31" cy="15" r="4" fill="#1e6b35"/></svg>
    <p>Poster print</p></div>
  <div class="service" style="left:593px;top:388px">
    <svg width="50" height="50" viewBox="0 0 50 50"><rect x="11" y="4" width="28" height="42" fill="#ffd500" stroke="#1e6b35" stroke-width="3"/><circle cx="25" cy="24" r="8" fill="#1e6b35"/></svg>
    <p>Greeting cards</p></div>
  <div class="service" style="left:812px;top:388px">
    <svg width="50" height="50" viewBox="0 0 50 50"><rect x="11" y="4" width="30" height="42" rx="3" fill="#1e6b35"/><rect x="18" y="11" width="17" height="28" fill="#ffd500"/><g fill="#ffd500"><rect x="6" y="9" width="9" height="3"/><rect x="6" y="17" width="9" height="3"/><rect x="6" y="25" width="9" height="3"/><rect x="6" y="33" width="9" height="3"/><rect x="6" y="41" width="9" height="3"/></g></svg>
    <p>Spiral bound books</p></div>

  <div class="btn" style="left:523px;top:553px;width:154px;height:33px">View more services</div>
</section>

<div class="mark" style="top:2136px"></div>
<h2 class="heading section-title" style="top:2167px">About us</h2>
<h3 class="abs heading welcome">Welcome to university</h3>
<div class="abs about-text">
  <p>University education is a company located in the campus, which has specialized in the service of school staff, as well as providing general public printing.</p>
  <p>Higher education publishes seminars and first-class textbooks for courses, prints theses for lesson, as well as working on an unprecedented number of smaller pieces for students, teachers and organizations. These include brochures, reports, questionnaires, business cards, books, OCR scanning and more.</p>
  <p>Higher education is a tailored print shop. The Green Leaf is the official eco-label of the Nordic countries, which has created a foothold in this country and is known among consumers.</p>
  <p>Vindaborgprent er staðsett á horninu á Lindargötu og Bakkagötu. (gengið inn Bakkagötumegin)</p>
</div>
<div class="btn" style="left:163px;top:2512px;width:108px;height:28px">Read more</div>
<div class="abs about-brand"><i></i>Vindaborgprent</div>

<div class="abs map" role="img" aria-label="Street map of the city centre with a location pin at the print shop"></div>
<div class="abs contact-panel"></div>
<div class="mark" style="top:2664px;left:867px"></div>
<h2 class="abs heading" style="left:600px;width:600px;text-align:center;top:2693px;font-size:29px">Send a wagon</h2>
<div class="field" style="top:2751px;height:42px">Name</div>
<div class="field" style="top:2802px;height:40px">Email</div>
<div class="field" style="top:2851px;height:121px">Massage</div>
<div class="btn" style="left:824px;top:2989px;width:108px;height:33px">Read more</div>
<div class="abs note" style="top:3039px">or</div>
<div class="abs note" style="top:3070px">Drag files in this window to send.</div>
<div class="btn" style="left:764px;top:3110px;width:107px;height:31px">Hætta</div>
<div class="btn" style="left:885px;top:3110px;width:105px;height:31px">Start sending</div>

<footer class="site-footer">
  <div class="abs footer-brand"><i></i>VINDABORGPRENT</div>
  <p class="abs footer-about">University education is a company located in the campus, which has specialized in the service of school staff, as well as providing general public printing.</p>
  <div class="abs footer-more">Read more</div>
  <div class="abs social"><i></i><i></i><i></i><i></i></div>

  <h2 class="abs heading footer-title" style="left:600px">Contact</h2>
  <ul class="abs links"><li>Home</li><li>Services</li><li>Job submit</li><li>About us</li><li>Contact us</li></ul>

  <h2 class="abs heading footer-title" style="left:873px">Contact</h2>
  <div class="info" style="top:148px">
    <svg width="18" height="18" viewBox="0 0 18 18"><path d="M4 1l3 4-2 2c1 2 3 4 5 5l2-2 4 3-2 3C8 16 2 10 1 4z" fill="#fff"/></svg>Tel: 555 0142</div>
  <div class="info" style="top:192px">
    <svg width="18" height="14" viewBox="0 0 18 14"><rect x="1" y="1" width="16" height="12" fill="none" stroke="#fff" stroke-width="1.6"/><path d="M1 1l8 7 8-7" fill="none" stroke="#fff" stroke-width="1.6"/></svg>verk@vindaborgprent.is</div>
  <div class="info" style="top:234px">
    <svg width="18" height="18" viewBox="0 0 18 18"><circle cx="9" cy="9" r="7.5" fill="none" stroke="#fff" stroke-width="1.6"/><path d="M9 4v5l3 2" fill="none" stroke="#fff" stroke-width="1.6"/></svg>Mon - Frí: 9-17</div>

  <div class="abs rule"></div>
  <div class="abs copy">© 2018 Vindaborgprent</div>
  <div class="abs cards"><i></i><i></i></div>
</footer>

</body>
</html>
```